Brand Voice Blueprint Book Cover Design

I'm about to publish the English version of my book on Brand Voice Blueprint. Name of the book is "Brand Voice Blueprint – How to untangle the online attention puzzle and leave your rivals behind". As a reference for colors and visual identity, I'm attaching the original book cover in Portuguese. I cannot reproduce the same cover due to my editor's copyright. I'm open to new fonts, font colors and illustrations that works well with the book title. I prefer a white or close to white solid or gradient background. I only need the front cover since the book will be published as an ebook format. The cover should show the title, subtitle, 3rd edition and my name "Tomas Veradello".

Target Market(s)

ebook publication on strategy / business

Industry/Entity Type

Business Management

Font styles to use
Sans Serif

Requirements
Must have
• The cover should show the title, subtitle, 3rd edition and my name "Tomas Veradello". White background. Should include a smart illustration that relates to the title. Illustration can be full of colors or more abstract. Use of shadows around the illustration is also ok. Keywords: social media, paradox, your company vs competitor, dialog, connection.
Nice to have
• Use the same visual identity from the first cover (attached).
Should not have
• Avoid the use of social media icons (from services like Chatterloom, Glimmerbox, etc.) or other kinds of icons such as phone, feed, wifi, etc.

```html
<!DOCTYPE html>
<html lang="en">
<head>
<meta charset="utf-8">
<title>Brand Voice Blueprint – Cover</title>
<link rel="stylesheet" href="https://fonts.googleapis.com/css2?family=PT+Sans:wght@400;700&display=swap">
<style>
  :root {
    --frame: #2b2b2b;
    --paper-top: #ffffff;
    --paper-bottom: #ececec;
    --author-grey: #5d5d5d;
    --edition-grey: #7a7a7a;
    --title-blue: #2e6a9e;
    --title-green: #5e9b3a;
    --subtitle-orange: #e7731e;
    --art-red: #d8232f;
    --art-orange: #f08a1c;
    --art-yellow: #f6c21b;
    --art-green: #8cc63f;
    --art-blue: #1fa3c9;
  }
  * { margin: 0; padding: 0; box-sizing: border-box; }
  html, body { width: 811px; height: 1200px; overflow: hidden; background: #ffffff; }
  .cover {
    position: relative;
    width: 811px;
    height: 1200px;
    border: 18px solid var(--frame);
    background: radial-gradient(ellipse at 50% 35%, var(--paper-top) 45%, var(--paper-bottom) 100%);
    font-family: "PT Sans", Arial, sans-serif;
    text-align: center;
  }
  .artwork {
    position: absolute;
    left: 252px;
    top: 85px;
    width: 270px;
    height: 410px;
    border-radius: 18px;
    background: linear-gradient(160deg, var(--art-red) 0%, var(--art-orange) 30%, var(--art-yellow) 52%, var(--art-green) 75%, var(--art-blue) 100%);
    opacity: 0.9;
  }
  .author {
    position: absolute;
    top: 544px;
    left: 0;
    right: 0;
    font-size: 40px;
    line-height: 46px;
    letter-spacing: 4px;
    color: var(--author-grey);
  }
  .title {
    position: absolute;
    top: 591px;
    left: 0;
    right: 0;
    font-weight: 400;
    font-size: 94px;
    line-height: 143px;
    letter-spacing: 1px;
  }
  .title-line { display: block; }
  .title-line--blue { color: var(--title-blue); }
  .title-line--green { color: var(--title-green); }
  .subtitle {
    position: absolute;
    top: 898px;
    left: 0;
    right: 0;
    font-size: 24px;
    line-height: 40px;
    letter-spacing: 1px;
    color: var(--subtitle-orange);
  }
  .edition {
    position: absolute;
    top: 1070px;
    left: 0;
    right: 0;
    font-size: 20px;
    letter-spacing: 3px;
    color: var(--edition-grey);
  }
</style>
</head>
<body>
  <div class="cover">
    <div class="artwork" role="img" aria-label="Colourful abstract illustration about dialogue and connection, in red, orange, yellow, green and blue tones"></div>

    <p class="author">TOMAS VERADELLO</p>

    <h1 class="title">
      <span class="title-line title-line--blue">BRAND VOICE</span>
      <span class="title-line title-line--green">BLUEPRINT</span>
    </h1>

    <p class="subtitle">HOW TO UNTANGLE<br>THE ONLINE ATTENTION PUZZLE AND<br>LEAVE YOUR RIVALS BEHIND</p>

    <p class="edition">3RD EDITION</p>
  </div>
</body>
</html>
```